Label and packaging - Lune de Sable

We are after label and pack design for a product called Lune de Sable. This product is a blend of Pinot Gris and Apple Cider.

Lune de Sable:

The packaging needs to accomplish the following: quickly explain what the product is, establish as a premium price product and grab the eye. The package should also reflect the product innovation.

Quickly Explain What the Product Is:

Lune de Sable is a nice name that could lift the image – but no one will have any idea what the product is by the name. Consider that a consumer will be staring at a shelf, then the bottle for maybe two to three seconds before moving on to another bottle. In those three seconds we need to make certain that they understand that the product is a blend of wine and cider. Lune de Sable will not support this on its own.

Suggestion is to use words like Wine, Cider, Orchard, Vine, Apple, Heirloom, Exotic and make it simple. Perhaps a sticker that says “50% Wine/50% Apple Cider” that sits on the neck of every bottle. They need to quickly ‘get it”. Imagery will assist as well. Consider a hybrid 50/50 image of wine grapes and apples to tell the story.

Establish a Premium Price Point:

The label needs to say high quality in the package and the font. Have fun with the shipper – this is where you can have a field day with imagery and fun buzz words – we love the idea of a busy shipper that tells the story with a clean and smart looking bottle.

Target Market(s)

This is a premium product targeted at females of age 25-45.

Industry/Entity Type

Consumer

Colors
ec1f27
9bcb3c

Requirements
Must have
• Label design on a burgundy bottle with a screw cap, see here for bottle shape: http://www.vr-bottlefolio.co.nz/wine/#/?view=thumbs&segments=41&colors=&capacityMin=187&capacityMax=750&heightMin=171&heightMax=334&labelMin=44&labelMax=168&neckMin=0&neckMax=1000

Packaging design on a 12 x 750ml carton. This sort of thing: https://www.casktrove.com.au/images/photo06.jpg

Nice to have
• We have attached some examples of a concept we quite like but it's not bright enough.

```html
<!DOCTYPE html>
<html lang="en">
<head>
<meta charset="utf-8">
<title>Lune de Sable – Label</title>
<link rel="stylesheet" href="https://fonts.googleapis.com/css2?family=Pinyon+Script&family=Italianno&family=Montserrat:wght@400&family=Petit+Formal+Script&display=swap">
<style>
  :root {
    --label-light: #efe98a;
    --label-mid: #dcd65a;
    --label-deep: #b9b635;
    --label-edge: #d9d59a;
    --ink: #111108;
    --apple-green: #7fb33a;
    --apple-deep: #4f8a25;
    --splash: #a9c27a;
  }
  html, body {
    margin: 0;
    padding: 0;
    width: 1000px;
    height: 1200px;
    overflow: hidden;
  }
  .label {
    position: relative;
    width: 1000px;
    height: 1200px;
    overflow: hidden;
    color: var(--ink);
    background:
      linear-gradient(90deg, rgba(0,0,0,0) 92%, var(--label-edge) 100%),
      radial-gradient(ellipse 60% 55% at 50% 70%, #f3eea0 0%, rgba(243,238,160,0) 100%),
      linear-gradient(180deg, #e6e05a 0%, var(--label-mid) 35%, var(--label-light) 75%, var(--label-mid) 100%);
  }
  .label__name {
    position: absolute;
    top: 58px;
    left: 0;
    width: 100%;
    margin: 0;
    text-align: center;
    font-family: "Pinyon Script", cursive;
    font-weight: 400;
    font-size: 104px;
    line-height: 1;
  }
  .label__hero {
    position: absolute;
    left: 85px;
    top: 235px;
    width: 820px;
    height: 600px;
  }
  .label__tagline {
    position: absolute;
    top: 888px;
    left: 0;
    width: 100%;
    margin: 0;
    text-align: center;
    font-family: "Petit Formal Script", cursive;
    font-size: 27px;
  }
  .label__origin {
    position: absolute;
    top: 950px;
    left: 0;
    width: 100%;
    margin: 0;
    text-align: center;
    font-family: "Montserrat", sans-serif;
    font-size: 24px;
    letter-spacing: 2px;
  }
  .label__volume,
  .label__abv {
    position: absolute;
    top: 1065px;
    margin: 0;
    font-family: "Pinyon Script", cursive;
    font-size: 72px;
    line-height: 1;
  }
  .label__volume { left: 78px; }
  .label__abv { right: 95px; }
</style>
</head>
<body>
  <main class="label">
    <h1 class="label__name">Lune de Sable</h1>

    <svg class="label__hero" viewBox="0 0 820 600" role="img" aria-label="Photograph of a green apple splashing into clear liquid">
      <defs>
        <radialGradient id="splash-fill" cx="50%" cy="55%" r="50%">
          <stop offset="0%" stop-color="#9dbf6e" stop-opacity="0.55"/>
          <stop offset="100%" stop-color="#a9c27a" stop-opacity="0"/>
        </radialGradient>
        <radialGradient id="apple-fill" cx="40%" cy="40%" r="60%">
          <stop offset="0%" stop-color="#8cc047"/>
          <stop offset="100%" stop-color="#4f8a25"/>
        </radialGradient>
      </defs>
      <ellipse cx="410" cy="320" rx="410" ry="290" fill="url(#splash-fill)"/>
      <ellipse cx="395" cy="360" rx="205" ry="185" fill="url(#apple-fill)" opacity="0.9"/>
    </svg>

    <p class="label__tagline">A full flavoured blend of Pinot Gris and Apple Cider</p>
    <p class="label__origin">PRODUCT OF NEW ZEALAND</p>

    <p class="label__volume">750ml</p>
    <p class="label__abv">9% Alc/Vol</p>
  </main>
</body>
</html>
```